Design for online reviews widget

Attached is a wireframe of a widget we need designing to display reviews on websites from multiple sources. We need this provided at 3 different sizes including full screen, contained (like the wireframe) and mobile.
You have completely free rein on the styling.
The only elements that should remain untouched are the blue stars (https://www.filquarry.net/s/8vtmwp2291zq4h/kv%20stars.ai?dl=0) and powered by logo at the bottom.
Ignore the menu at the top of the wireframe, this is just from the website the widget will be placed on.
Businesses

```html
<!DOCTYPE html>
<html lang="en">
<head>
<meta charset="utf-8">
<title>Reviews Widget</title>
<link href="https://fonts.googleapis.com/css2?family=Nunito:wght@400;600;700;800&display=swap" rel="stylesheet">
<style>
:root{
  --page:#f8f8f8;
  --panel:#ffffff;
  --card:#f0f0f0;
  --title:#2a7fa8;
  --ink:#1e1e1e;
  --meta:#8c7355;
  --muted:#a9a9a9;
  --accent:#3cb8e6;
  --gold:#f7b90f;
  --score:#0b4f9c;
  --green:#008a55;
  --brand:#333333;
}
*{box-sizing:border-box;margin:0;padding:0}
html,body{width:763px;height:1200px;overflow:hidden;background:var(--page);font-family:'Nunito',sans-serif;color:var(--ink)}
body{position:relative}
.widget{position:absolute;left:77px;top:37px;width:611px;height:1163px;background:var(--panel);border-radius:18px 18px 0 0;overflow:hidden}
.summary{position:absolute;left:0;right:0;top:27px;text-align:center}
.summary-stars{display:flex;justify-content:center;gap:4px}
.summary-score{margin-top:12px;font-size:9.5px}
.filter{position:absolute;right:10px;top:60px;width:135px;height:26px;border-radius:13px;background:#f7f7f7;color:var(--muted);font-size:9px;display:flex;align-items:center;justify-content:flex-end;padding-right:14px;gap:6px}
.review{position:absolute;left:9px;width:592px;background:var(--card);border-radius:6px;box-shadow:0 2px 3px rgba(0,0,0,.06);padding:16px 18px}
.review-title{font-size:14.5px;font-weight:700;color:var(--title);line-height:20px}
.review-body{width:418px;margin-top:12px;font-size:10px;line-height:22px}
.ratings{display:flex;margin-top:12px;font-size:10.5px}
.ratings span{display:inline-block}
.ratings span:nth-child(1){width:109px}
.ratings span:nth-child(2){width:97px}
.ratings span:nth-child(3){width:102px}
.ratings b,.service b{color:var(--title);font-weight:700}
.service{margin-top:14px;font-size:10.5px}
.review-meta{margin-top:16px;font-size:9.5px;font-weight:700;color:var(--meta)}
.source{position:absolute;right:14px;width:150px;text-align:center}
.source-name{font-size:17px;font-weight:800;color:var(--brand);line-height:1.2}
.source-stars{display:flex;justify-content:center;gap:6px;margin-top:10px;fill:var(--gold)}
.score-ring{margin:18px auto 0;width:80px;height:80px;border-radius:50%;border:4px solid var(--score);display:flex;align-items:center;justify-content:center}
.score-ring span{width:64px;height:64px;border-radius:50%;background:var(--score);color:#fff;font-size:21px;font-weight:800;display:flex;align-items:center;justify-content:center}
.load-more{position:absolute;left:219px;top:1068px;width:173px;height:37px;border-radius:5px;background:var(--green);color:#fff;font-size:15px;font-weight:800;display:flex;align-items:center;justify-content:center}
.powered{position:absolute;left:492px;top:1114px;font-size:7px}
.powered-name{display:flex;align-items:center;gap:5px;margin-top:8px;font-size:13px;font-weight:800;color:#222}
.powered-name i{width:12px;height:12px;border-radius:50%;background:var(--accent);display:inline-block}
</style>
</head>
<body>
<svg width="0" height="0" style="position:absolute">
  <defs>
    <symbol id="star" viewBox="0 0 24 24"><path d="M12 2l2.9 6.9 7.1.6-5.4 4.7 1.7 7.1L12 17.5 5.7 21.3l1.7-7.1L2 9.5l7.1-.6z"/></symbol>
    <symbol id="badge-star" viewBox="0 0 26 26"><circle cx="13" cy="13" r="13" fill="#3cb8e6"/><path d="M13 5.5l2.1 4.9 5.3.5-4 3.5 1.2 5.2L13 16.8l-4.6 2.8 1.2-5.2-4-3.5 5.3-.5z" fill="#fff"/></symbol>
  </defs>
</svg>

<main class="widget">
  <section class="summary">
    <div class="summary-stars" aria-label="Five star rating">
      <svg width="26" height="26"><use href="#badge-star"/></svg>
      <svg width="26" height="26"><use href="#badge-star"/></svg>
      <svg width="26" height="26"><use href="#badge-star"/></svg>
      <svg width="26" height="26"><use href="#badge-star"/></svg>
      <svg width="26" height="26"><use href="#badge-star"/></svg>
    </div>
    <p class="summary-score">Combined Review Score 4.3 out of 5</p>
  </section>
  <div class="filter">Filter Results
    <svg width="10" height="6" viewBox="0 0 10 6"><path d="M1 1l4 4 4-4" fill="none" stroke="#3cb8e6" stroke-width="1.5"/></svg>
  </div>

  <article class="review" style="top:97px;height:218px">
    <h2 class="review-title">Front Door With Windows Each Side And Side Window</h2>
    <p class="review-body">This is the second time we have used regent home Improvments , and the service is amazing! Owen came round several times as we keep changing our minds and he was so helpful and gave us good advice, and the guys who do the fitting are &nbsp;efficient and tidy . I’ve got to say the end result is amazing and I have recommended to many of friends . Thanks Regent</p>
    <div class="ratings">
      <span><b>Reliablity:</b> 9.38</span>
      <span><b>Courtesy:</b> 10</span>
      <span><b>Tidiness:</b> 9.84</span>
      <span><b>Workmanship:</b> 10</span>
    </div>
    <p class="review-meta">Verified 28th September 2021 | Located In Ashford</p>
    <div class="source" style="top:44px">
      <div class="source-name">Tandrivo</div>
      <div class="score-ring"><span>9.77</span></div>
    </div>
  </article>

  <article class="review" style="top:335px;height:239px">
    <h2 class="review-title">Positive: Professionalism, Quality, Value</h2>
    <p class="review-body">The team did a good job of replacing a large feature window spanning two floors, as well as the others in my property. They're a professional group who were willing to work out solutions to any problem, especially compared to other companies. Prices are fair, and my new UPVC windows look great. Special thanks to Frank for being so accommodating and for the good communication throughout.</p>
    <p class="service"><b>Service:</b> Window installation</p>
    <p class="review-meta">11 Months Ago By Dana Holt</p>
    <div class="source" style="top:66px">
      <div class="source-name" style="font-size:24px">Quellbyn</div>
      <div class="source-stars">
        <svg width="20" height="20"><use href="#star"/></svg><svg width="20" height="20"><use href="#star"/></svg><svg width="20" height="20"><use href="#star"/></svg><svg width="20" height="20"><use href="#star"/></svg><svg width="20" height="20"><use href="#star"/></svg>
      </div>
    </div>
  </article>

  <article class="review" style="top:594px;height:217px">
    <h2 class="review-title">Brilliant All Round Professional, Friendly Service.</h2>
    <p class="review-body">This home run friendly business was a real pleasure to deal with. From the professional, no pressure quote, nothing was too much trouble to ensure everything is as required for your needs with the quote and fitting. The workmanship and double glazing being fitted was brilliant and my home/outdoors was left tidy and clean leaving an outstanding impression for such an all round professional job. I would not hesitate to recommend this company, such a brilliant service from great hardworking people that care about their service.</p>
    <p class="review-meta" style="margin-top:10px">13 Feb 2018 By GreenChair41</p>
    <div class="source" style="top:66px">
      <div class="source-name" style="font-size:24px">Vornmere</div>
      <div class="source-stars">
        <svg width="20" height="20"><use href="#star"/></svg><svg width="20" height="20"><use href="#star"/></svg><svg width="20" height="20"><use href="#star"/></svg><svg width="20" height="20"><use href="#star"/></svg><svg width="20" height="20"><use href="#star"/></svg>
      </div>
    </div>
  </article>

  <article class="review" style="top:832px;height:181px">
    <h2 class="review-title">Front Door With Windows Each Side And Side Window</h2>
    <p class="review-body">This is the second time we have used regent home Improvments , and the service is amazing! Owen came round several times as we keep changing our minds and he was so helpful and gave us good advice, and the guys who do the fitting are &nbsp;efficient and tidy . I’ve got to say the end result is amazing and I have recommended to many of friends . Thanks Regent</p>
    <p class="review-meta" style="margin-top:10px">13 Feb 2018 By Ruth</p>
    <div class="source" style="top:58px">
      <div class="source-name" style="font-size:20px">Pellastro</div>
      <div class="source-stars">
        <svg width="20" height="20"><use href="#star"/></svg><svg width="20" height="20"><use href="#star"/></svg><svg width="20" height="20"><use href="#star"/></svg><svg width="20" height="20"><use href="#star"/></svg><svg width="20" height="20"><use href="#star"/></svg>
      </div>
    </div>
  </article>

  <div class="load-more">LOAD MORE</div>

  <div class="powered">
    <p>Powered by</p>
    <div class="powered-name"><i></i>Zorvanti</div>
  </div>
</main>
</body>
</html>
```